Best Seller Book Cover ...

Book Title: Skip the Big Answer: Pick a Trail, Keep to That Trail, Mind the Geese

Edgy, Minimalist, Compelling, Attractive, Classy design.

Very clean. See examples.,

Target Market(s)

Mid Life People ages 38-55 Male and Female equally

• Nice to Have:

Minimalist and eye catching ( i have loaded a few examples of what this means)
Should not have
• Clip Art
Clutter

```html
<!DOCTYPE html>
<html lang="en">
<head>
<meta charset="utf-8">
<title>Skip the Big Answer – Book Cover Spread</title>
<link href="https://fonts.googleapis.com/css2?family=Oswald:wght@500;600;700&family=Arimo:wght@400&display=swap" rel="stylesheet">
<style>
  :root {
    --page: #ffffff;
    --orange: #e2602f;
    --orange-light: #ec7440;
    --orange-dark: #cf4a22;
    --white: #ffffff;
    --ink-dark: #3b1408;
    --display: "Oswald", "Arial Narrow", sans-serif;
    --body: "Arimo", Arial, sans-serif;
  }
  * { margin: 0; padding: 0; box-sizing: border-box; }
  html, body { width: 817px; height: 1200px; overflow: hidden; background: var(--page); }
  .canvas { position: relative; width: 817px; height: 1200px; }

  .spread {
    position: absolute; left: 7px; top: 339px; width: 802px; height: 522px;
    background: radial-gradient(ellipse at 70% 55%, var(--orange-light) 0%, var(--orange) 45%, var(--orange-dark) 100%);
    color: var(--white);
    overflow: hidden;
  }
  .spread-lines { position: absolute; inset: 0; }

  /* back cover */
  .back-quotes { position: absolute; left: 58px; top: 42px; width: 262px; }
  .quote { font-family: var(--body); font-size: 10.6px; line-height: 14.4px; text-align: justify; text-indent: 10px; }
  .quote-author { font-family: var(--body); font-size: 10.6px; text-align: right; margin: 14px 8px 36px 0; }

  /* spine */
  .spine-title, .spine-sub, .spine-author {
    position: absolute; writing-mode: vertical-rl; white-space: nowrap;
    font-family: var(--display);
  }
  .spine-title { left: 366px; top: 40px; font-size: 38px; font-weight: 600; line-height: 36px; }
  .spine-sub { left: 395px; top: 128px; font-size: 11px; font-weight: 600; line-height: 14px; color: var(--ink-dark); }
  .spine-author { left: 395px; top: 400px; font-size: 13px; font-weight: 600; }

  /* front cover */
  .front-title {
    position: absolute; left: 430px; width: 365px; top: 112px;
    text-align: center; white-space: nowrap;
    font-family: var(--display); font-size: 150px; font-weight: 600; line-height: 150px; letter-spacing: -1px;
  }
  .front-subtitle {
    position: absolute; left: 420px; width: 380px; top: 300px; text-align: center;
    font-family: var(--display); font-size: 15.5px; font-weight: 600; line-height: 27px; color: var(--ink-dark);
  }
  .front-author {
    position: absolute; left: 430px; width: 365px; top: 456px; text-align: center;
    font-family: var(--display); font-size: 19px; font-weight: 600;
  }
</style>
</head>
<body>
<div class="canvas">
  <section class="spread">
    <svg class="spread-lines" width="802" height="522" viewBox="0 0 802 522" aria-hidden="true">
      <polyline points="470,88 478,52 712,14" fill="none" stroke="#ffffff" stroke-width="2.5"/>
      <line x1="716" y1="12" x2="725" y2="58" stroke="#ffffff" stroke-width="1.5"/>
      <line x1="620" y1="396" x2="593" y2="418" stroke="#ffffff" stroke-width="1.2"/>
      <line x1="232" y1="456" x2="258" y2="470" stroke="#ffffff" stroke-width="1"/>
    </svg>

    <div class="back-quotes">
      <p class="quote">All good books are alike in that they are truer than if they had really happened and after you are finished reading one you will feel that all that happened to you and afterwards it all belongs to you: the good and the bad, the ecstasy, the remorse and sorrow, the people and the places and how the weather was.</p>
      <p class="quote-author">Walter Brannock</p>
      <p class="quote">A book is a fragile creature, it suffers the wear of time, it fears rodents, the elements and clumsy hands. so the librarian protects the books not only against mankind but also against nature and devotes his life to this war with the forces of oblivion.</p>
      <p class="quote-author">Lucio Ferrante</p>
      <p class="quote">Every reader finds himself. The writer's work is merely a kind of optical instrument that makes it possible for the reader to discern what, without this book, he would perhaps never have seen in himself.</p>
      <p class="quote-author">Henri Devalle</p>
    </div>

    <div class="spine-title">SKIP</div>
    <div class="spine-sub">the Big Answer: Pick a Trail, Keep to That Trail,<br>Mind the Geese</div>
    <div class="spine-author">DANIEL R. WHITMORE</div>

    <h1 class="front-title">SKIP</h1>
    <p class="front-subtitle">the Big Answer: Pick a Trail, Keep to That Trail,<br>Mind the Geese</p>
    <p class="front-author">DANIEL R. WHITMORE</p>
  </section>
</div>
</body>
</html>
```